Harbor of Kellvane - Lanternsdag Poster Design

We need a poster (8.5" x 11") for our Lanternsdag Celebration event June 18 - 19, 2016. I've included the Port logo, event logo, content, and some photos to choose from. Not all the photos have to be used, though. Feel free to use, crop and size photos how you see fit. Colors and fonts are also up to you. Looking for a fun design that screams family fun event!

Target Market(s)

Families

Industry/Entity Type

Event

Requirements
Must have
• The event logo, the Port logo, some photos (provided) and the content provided.

```html
<!DOCTYPE html>
<html lang="en">
<head>
<meta charset="utf-8">
<title>Lanternsdag Celebration Poster</title>
<link href="https://fonts.googleapis.com/css2?family=Oswald:wght@300;500;700&family=Roboto:ital,wght@1,900&family=Roboto+Condensed:wght@400&family=Open+Sans:wght@400;700&display=swap" rel="stylesheet">
<style>
  :root{
    --red:#e4232b;
    --blue:#1a55c4;
    --blue-deep:#0f3c9e;
    --navy:#1c2a6b;
    --white:#ffffff;
    --ink:#3a3a3a;
    --stage:#2b2b2b;
  }
  html,body{margin:0;padding:0;overflow:hidden}
  body{width:900px;height:1200px;background:var(--stage);position:relative}
  .poster{position:absolute;left:60px;top:100px;width:780px;height:1000px;background:var(--white);overflow:hidden;box-shadow:0 10px 30px rgba(0,0,0,.5)}
  .hero-photo{position:absolute;left:0;top:0;width:780px;height:460px;
    background:linear-gradient(90deg,#6f7a78 0%,#8c8480 30%,#a9aeb4 55%,#e9ecef 75%,#fff 88%);
    clip-path:polygon(0 0,100% 0,100% 238px,0 440px)}
  .bands{position:absolute;left:0;top:0}
  .event-mark{position:absolute;left:535px;top:60px;width:220px;text-align:center;
    font-family:'Oswald',sans-serif;font-weight:700;font-size:40px;color:var(--navy);display:flex;align-items:center;justify-content:center;gap:10px}
  .event-mark .dot{width:16px;height:16px;border-radius:50%;background:var(--red)}
  .title-box{position:absolute;left:172px;top:270px;width:460px;height:140px;margin:0;background:var(--red);
    transform:rotate(-12deg);transform-origin:center;box-shadow:0 0 0 4px var(--white);
    font-family:'Oswald',sans-serif;color:var(--white);text-align:center;line-height:1;z-index:2}
  .title-box .kicker{display:block;font-weight:300;font-size:44px;margin-top:12px;letter-spacing:.5px}
  .title-box .main{display:block;font-weight:700;font-size:76px;margin-top:2px}
  .date-line{position:absolute;left:20px;top:462px;width:740px;height:40px;margin:0;text-align:center;
    font-family:'Roboto',sans-serif;font-style:italic;font-weight:900;font-size:34px;line-height:40px;color:var(--white);
    transform:rotate(-8deg);transform-origin:center;letter-spacing:1px;white-space:nowrap;z-index:3}
  .date-line .sep{color:var(--red);margin:0 8px}
  .photo{position:absolute;border:5px solid var(--white);box-sizing:border-box;box-shadow:0 0 0 2px var(--red);z-index:1}
  .photo-picnic{left:0;top:558px;width:208px;height:147px;background:linear-gradient(160deg,#b9c2c6,#6f675c 60%,#4b4440)}
  .photo-music{left:235px;top:525px;width:232px;height:180px;background:linear-gradient(160deg,#b8c0a8,#5b5c52 55%,#2a2a2a)}
  .photo-derby{left:503px;top:490px;width:277px;height:215px;background:linear-gradient(175deg,#e8ece9,#8f8f88 45%,#7f8677 75%,#6b6d60)}
  .red-rule{position:absolute;left:0;top:705px;width:780px;height:17px;background:var(--red)}
  .day-one{position:absolute;left:0;top:722px;width:780px;height:158px;background:linear-gradient(90deg,var(--blue-deep),var(--blue) 60%,var(--blue-deep))}
  .day-label{position:absolute;left:28px;font-family:'Oswald',sans-serif;font-weight:500;font-size:40px;line-height:42px;width:90px;text-align:center}
  .day-label sup{font-size:20px;vertical-align:top;position:relative;top:4px}
  .day-one .day-label{top:28px;color:var(--white)}
  .divider{position:absolute;left:125px;width:3px}
  .day-one .divider{top:20px;height:118px;background:var(--white)}
  .col{position:absolute;top:14px;color:var(--white)}
  .col h3{margin:0 0 10px;font-family:'Open Sans',sans-serif;font-weight:700;font-size:16px;line-height:20px}
  .col ul{margin:0;padding:0;list-style:none;font-family:'Roboto Condensed',sans-serif;font-size:13.5px;line-height:19.5px}
  .col li{position:relative;padding-left:19px}
  .col li::before{content:"";position:absolute;left:3px;top:7px;width:6px;height:6px;border-radius:50%;background:var(--red)}
  .col-family{left:159px}
  .col-kids{left:310px}
  .col-kids h3,.col-norse h3{margin-top:10px;margin-bottom:14px}
  .col-norse{left:464px}
  .day-two{position:absolute;left:0;top:880px;width:780px;height:120px}
  .day-two .day-label{top:14px;color:var(--red)}
  .day-two .divider{top:16px;height:78px;background:var(--red)}
  .trail{position:absolute;left:159px;top:26px;width:245px}
  .trail h3{margin:0;font-family:'Open Sans',sans-serif;font-weight:700;font-size:16px;line-height:22px;color:var(--blue);white-space:nowrap}
  .trail p{margin:2px 0 0;font-family:'Open Sans',sans-serif;font-size:14px;line-height:18px;color:var(--ink)}
  .info-panel{position:absolute;left:0;top:0}
  .info-text{position:absolute;left:450px;top:22px;width:330px;text-align:center;color:var(--white);font-family:'Open Sans',sans-serif;font-weight:700}
  .info-text .lead{font-size:17px;line-height:22px}
  .info-text .phone{font-size:22px;line-height:30px;margin-top:4px}
  .info-text .web{font-size:10px;line-height:14px}
</style>
</head>
<body>
<main class="poster">
  <div class="hero-photo" role="img" aria-label="Festival photo: folk dancers in traditional costume dancing in a circle at the marina"></div>

  <svg class="bands" width="780" height="705" viewBox="0 0 780 705" aria-hidden="true">
    <polygon points="0,440 780,238 780,262 0,464" fill="var(--red)"/>
    <polygon points="0,470 780,268 780,480 0,548" fill="var(--blue)"/>
    <polygon points="0,552 780,484 780,494 0,562" fill="var(--red)"/>
  </svg>

  <div class="event-mark"><span class="dot"></span>Lanternsdag</div>

  <div class="photo photo-picnic" role="img" aria-label="Photo: families seated at picnic tables under a tent"></div>
  <div class="photo photo-music" role="img" aria-label="Photo: musician playing acoustic guitar at a microphone"></div>
  <div class="photo photo-derby" role="img" aria-label="Photo: children fishing at the derby pool under a canopy"></div>

  <h1 class="title-box"><span class="kicker">LANTERNSDAG</span><span class="main">CELEBRATION</span></h1>

  <p class="date-line">JUNE 18 -19<span class="sep">|</span>AT THE KELLVANE MARINA</p>

  <div class="red-rule"></div>

  <section class="day-one">
    <div class="day-label">JUNE<br>18<sup>TH</sup></div>
    <div class="divider"></div>
    <div class="col col-family">
      <h3>Fun for the<br>whole family</h3>
      <ul><li>2-for-1 Moorage</li><li>Live Music</li><li>Hot Dog Vendor</li><li>Power Squadron</li></ul>
    </div>
    <div class="col col-kids">
      <h3>Kid’s Activities</h3>
      <ul><li>Fishing Derby</li><li>Touch a Fire Truck</li><li>Toy Boat Building</li></ul>
    </div>
    <div class="col col-norse">
      <h3>Traditional Norwegian Activities</h3>
      <ul><li>Raising the Mai “Green” Stang</li><li>Traditional Norwegian Food and Dancing</li><li>Bonfire Lighting with the Kellvane Vikings</li></ul>
    </div>
  </section>

  <section class="day-two">
    <div class="day-label">JUNE<br>19<sup>TH</sup></div>
    <div class="divider"></div>
    <div class="trail">
      <h3>Brisk Water Trails Festival</h3>
      <p>Keys to Ashport Fun Paddle A fun event for paddlers of all levels!</p>
    </div>
    <svg class="info-panel" width="780" height="120" viewBox="0 0 780 120" aria-hidden="true">
      <polygon points="412,0 444,0 426,120 394,120" fill="var(--blue)"/>
      <polygon points="446,0 780,0 780,120 428,120" fill="var(--red)"/>
    </svg>
    <div class="info-text">
      <div class="lead">For more information,</div>
      <div class="phone">lease call (360) 555-0142</div>
      <div class="web">On the web at www.harborofkellvane.com/lanternsdag-2</div>
    </div>
  </section>
</main>
</body>
</html>
```